Business card design for Plumbing and Gas fitting company

We need a business card design for our plumbing and gas fitting company using the company logo and director details. Design should be modern and eye-catching however kept reasonably simple. This design should be targeted at commercial businesses/work so professionalism is key.

Target Market(s)

Commercial/business

Industry/Entity Type

Plumbing

Contact Information for Business Card

Warren Dohey
Director
027 581 9043
warren@vantorplumbingandgas.example
PO Box 7816
Palmerston North 4472

Font styles to use
Sans Serif

Requirements
Must have
• Logo
• Modern
• Kept simple
Nice to have
• Colour scheme based around logo

```html
<!DOCTYPE html>
<html lang="en">
<head>
<meta charset="utf-8">
<title>Vantor Plumbing &amp; Gas — Business Card</title>
<link rel="stylesheet" href="https://fonts.googleapis.com/css2?family=Oswald:wght@300;400;600&display=swap">
<style>
  :root {
    --backdrop: #e9e6e7;
    --card-white: #ffffff;
    --card-black: #050505;
    --brand-blue: #1170b8;
    --brand-orange: #e57a2e;
    --text-light: #f4f4f4;
    --text-muted: #cfcfcf;
    --shadow: rgba(40, 30, 35, 0.25);
  }
  * { margin: 0; padding: 0; box-sizing: border-box; }
  html, body {
    width: 1200px;
    height: 675px;
    overflow: hidden;
    background: var(--backdrop);
    font-family: "Oswald", "Arial Narrow", sans-serif;
  }
  .sheet {
    width: 1200px;
    height: 675px;
    display: flex;
    align-items: center;
    justify-content: center;
    gap: 56px;
  }
  .card {
    width: 525px;
    height: 300px;
    position: relative;
    box-shadow: 0 10px 28px var(--shadow);
    overflow: hidden;
  }
  .card--front {
    background: var(--card-white);
    display: flex;
    align-items: center;
    justify-content: center;
  }
  .brand {
    display: flex;
    align-items: center;
    gap: 14px;
  }
  .brand__dot {
    width: 30px;
    height: 30px;
    border-radius: 50%;
    background: var(--brand-orange);
  }
  .brand__name {
    font-weight: 600;
    font-size: 34px;
    letter-spacing: 0.5px;
    color: var(--brand-blue);
  }
  .card--back {
    background: var(--card-black);
    color: var(--text-light);
    padding: 62px 0 0 62px;
  }
  .person {
    border-left: 3px solid var(--brand-blue);
    padding-left: 14px;
    margin-bottom: 44px;
  }
  .person__name {
    font-weight: 600;
    font-size: 30px;
    line-height: 1.05;
    text-transform: uppercase;
    letter-spacing: 0.3px;
  }
  .person__role {
    font-weight: 300;
    font-size: 17px;
    color: var(--text-muted);
  }
  .contact {
    list-style: none;
    font-weight: 300;
    font-size: 19px;
    line-height: 1.3;
  }
  .contact__row {
    display: flex;
  }
  .contact__label {
    font-weight: 400;
    width: 32px;
    flex-shrink: 0;
  }
</style>
</head>
<body>
  <main class="sheet">
    <section class="card card--front" aria-label="Business card front">
      <div class="brand">
        <span class="brand__dot"></span>
        <span class="brand__name">Vantor Plumbing &amp; Gas</span>
      </div>
    </section>

    <section class="card card--back" aria-label="Business card back">
      <div class="person">
        <h1 class="person__name">Warren Dohey</h1>
        <p class="person__role">Director</p>
      </div>
      <ul class="contact">
        <li class="contact__row"><span class="contact__label">P:</span><span>027 581 9043</span></li>
        <li class="contact__row"><span class="contact__label">M:</span><span>warren@vantorplumbingandgas.example</span></li>
        <li class="contact__row"><span class="contact__label">A:</span><span>PO Box 7816<br>Palmerston North 4472</span></li>
      </ul>
    </section>
  </main>
</body>
</html>
```